M Website

We need a website design for a construction plant company. You may use a combination of our photos and the stock images. See the logo for company colours. It also be of great value to see moving pictures like the ones on the link: https://www.quindellworks.co.za/copy-of-about-us. See our uploaded files for content.

Target Market(s)

Construction

Number of Pages Required

5+ page

```html
<!DOCTYPE html>
<html lang="en">
<head>
<meta charset="utf-8">
<title>Kestrel Logistics and Plant Hire</title>
<link href="https://fonts.googleapis.com/css2?family=Lato:wght@400;700;900&family=Montserrat:wght@500;600;700&display=swap" rel="stylesheet">
<style>
:root{
  --dark:#3f3f3f;
  --yellow:#f5c21b;
  --ink:#3a3a3a;
  --text:#555;
  --band:#e4e4e4;
  --white:#fff;
  --nav-active:#8a7a7f;
}
*{box-sizing:border-box;margin:0;padding:0}
html,body{width:1124px;height:1200px;overflow:hidden;background:var(--white)}
body{position:relative;font-family:'Lato',sans-serif;color:var(--ink)}
.topbar{position:absolute;left:0;top:0;width:1124px;height:117px;background:var(--dark)}
.brand{position:absolute;left:92px;top:14px;display:flex;align-items:center;gap:8px;color:var(--yellow);font-family:'Montserrat',sans-serif;font-weight:700;font-size:20px}
.brand-dot{width:14px;height:14px;border-radius:50%;background:var(--yellow)}
.contact-info{position:absolute;right:92px;top:20px;display:flex;align-items:center;gap:18px;font-family:'Montserrat',sans-serif;font-weight:500;font-size:10.5px;color:var(--white);letter-spacing:-.2px}
.info-item{display:flex;align-items:center;gap:6px;line-height:1.35}
.info-item svg{flex:none}
.main-nav{position:absolute;left:92px;top:76px;width:940px;height:74px;background:var(--white);display:flex;justify-content:center;align-items:center;gap:63px;z-index:2;font-family:'Montserrat',sans-serif;font-weight:600;font-size:13px;letter-spacing:.4px;color:var(--ink)}
.main-nav .active{color:var(--nav-active)}
.hero{position:absolute;left:0;top:117px;width:1124px;height:616px;background:linear-gradient(160deg,#4a4a48 0%,#3a3936 45%,#2e2d2a 100%);display:flex;flex-direction:column;align-items:center}
.hero h1{margin-top:138px;text-align:center;color:var(--white);font-weight:700;font-size:63px;line-height:72px;letter-spacing:-1.5px}
.btn-primary{margin-top:30px;width:216px;height:73px;background:var(--yellow);color:#2a2a2a;font-family:'Montserrat',sans-serif;font-weight:700;font-size:25px;display:flex;align-items:center;justify-content:center;letter-spacing:.5px}
.quote-band{position:absolute;left:0;top:733px;width:1124px;height:85px;background:var(--band);display:flex;align-items:center;justify-content:space-between;padding:0 92px 0 91px}
.quote-band p{font-size:26px;color:#4a4a4a;letter-spacing:-.2px}
.btn-quote{width:160px;height:49px;background:var(--yellow);display:flex;align-items:center;justify-content:center;font-size:20px;color:#2d2d2d}
.about{position:absolute;left:93px;top:844px;width:540px}
.about h2{font-weight:700;font-size:26px;line-height:32px;color:var(--ink);letter-spacing:-.2px}
.about h2 .accent{color:var(--yellow)}
.about p{margin-top:20px;font-size:12.6px;line-height:25.7px;color:var(--text)}
.about-photo{position:absolute;left:736px;top:851px;width:296px;height:169px;background:linear-gradient(120deg,#9aa3ad 0%,#4f6a92 45%,#c23a3a 85%)}
.why{position:absolute;left:93px;top:1130px}
.why h2{font-weight:700;font-size:26px;color:var(--ink);letter-spacing:-.2px}
.why-underline{margin-top:6px;width:114px;height:3px;background:var(--yellow)}
</style>
</head>
<body>
<header class="topbar">
  <div class="brand"><span class="brand-dot"></span>Kestrel</div>
  <div class="contact-info">
    <div class="info-item">
      <svg width="18" height="22" viewBox="0 0 18 22" fill="none" stroke="#f5c21b" stroke-width="1.6"><path d="M9 21s7-7.2 7-12A7 7 0 0 0 2 9c0 4.8 7 12 7 12z"/><circle cx="9" cy="9" r="2.6"/></svg>
      <span>P.O Box 410, Fernvale, 2194<br>12 Acacia Road, Fernvale, 2194</span>
    </div>
    <div class="info-item">
      <svg width="20" height="20" viewBox="0 0 24 24" fill="none" stroke="#f5c21b" stroke-width="1.6"><path d="M5 3h4l2 5-2.5 1.5a11 11 0 0 0 6 6L16 13l5 2v4a2 2 0 0 1-2 2A17 17 0 0 1 3 5a2 2 0 0 1 2-2z"/><path d="M14 3a7 7 0 0 1 7 7M14 7a3 3 0 0 1 3 3"/></svg>
      <span>+27 (0) 11 555 0142</span>
    </div>
    <div class="info-item">
      <svg width="26" height="20" viewBox="0 0 26 20" fill="none" stroke="#f5c21b" stroke-width="1.6"><rect x="1" y="1" width="24" height="18"/><path d="M1 1l12 10L25 1M1 19l9-8M25 19l-9-8"/></svg>
      <span>info@kestrellogistics.co.za</span>
    </div>
  </div>
</header>
<nav class="main-nav">
  <span class="active">HOME</span><span>ABOUT</span><span>COMPANY</span><span>OUR SERVICES</span><span>NEWS</span><span>CONTACT</span>
</nav>
<section class="hero" role="img" aria-label="Workers tying steel rebar mesh on a construction site">
  <h1>Delivering high quality<br>multidisciplinary engineering<br>and construction projects</h1>
  <div class="btn-primary">Contact us</div>
</section>
<section class="quote-band">
  <p>Looking for Quality and affordable Constructer for your project ?</p>
  <div class="btn-quote">Get a Quote</div>
</section>
<section class="about">
  <h2>With Over <span class="accent">&nbsp;5+&nbsp; Years</span> Experience Rest Assured You’re in Safe Hands</h2>
  <p>Kestrel Logistics and Plant Hire (Pty) Ltd is a Black Woman owned Construction and Plant Hire company operating mainly from the Kestrel head office in Fernvale Gauteng. Kestrel Logistics and Plant Hire (Pty) Ltd was established in 2014, and has worked in various municipal jurisdictions within South Africa.</p>
</section>
<div class="about-photo" role="img" aria-label="Two engineers in hard hats reviewing plans on site"></div>
<section class="why">
  <h2>Why&nbsp; You Should Choose Us</h2>
  <div class="why-underline"></div>
</section>
</body>
</html>
```